Need a new letterhead

Need a new fresh exciting letterhead. Remove the footer...info is outdated.

Target Market(s)

B2B

Industry/Entity Type

Electrical Power

Colors

Designer to choose colors to be used in the design.

Requirements
Must have
• Red and Blue Corvane Systems Logo
Nice to have
• Lighting the way to sustainability in footer...reorganize the words?

```html
<!DOCTYPE html>
<html lang="en">
<head>
<meta charset="utf-8">
<title>Corvane Systems Letterhead</title>
<link href="https://fonts.googleapis.com/css2?family=Lato:wght@400;700;900&display=swap" rel="stylesheet">
<style>
  :root {
    --backdrop: #cfc3bf;
    --paper: #fffefb;
    --brand-red: #ec1c24;
    --brand-blue: #1c2f8c;
    --mark-warm: #fbf3dc;
    --mark-green: #e6f1e6;
  }
  * { margin: 0; padding: 0; box-sizing: border-box; }
  html, body {
    width: 1200px; height: 784px; overflow: hidden;
    background: var(--backdrop);
    font-family: "Lato", sans-serif;
  }
  .stage {
    width: 1200px; height: 784px;
    display: flex; align-items: center; justify-content: center;
  }
  .letterhead {
    position: relative;
    width: 560px; height: 724px;
    background: var(--paper);
    box-shadow: 0 6px 18px rgba(60, 40, 40, 0.25);
    overflow: hidden;
  }
  .brand {
    position: absolute; top: 40px; left: 150px;
    display: flex; align-items: center; gap: 10px;
  }
  .brand-dot {
    width: 12px; height: 12px; border-radius: 50%;
    background: var(--brand-blue);
    flex: none;
  }
  .brand-name {
    font-weight: 900; font-size: 22px; letter-spacing: 0.5px;
    color: var(--brand-red); text-transform: uppercase; line-height: 1.05;
  }
  .contact {
    position: absolute; top: 150px; right: 36px;
    font-style: normal; font-size: 10px; line-height: 1.5;
  }
  .contact .address { color: var(--brand-red); margin-bottom: 3px; }
  .contact .line {
    display: flex; align-items: center; gap: 6px; color: var(--brand-blue);
  }
  .contact svg { width: 9px; height: 9px; flex: none; }
  .watermark {
    position: absolute; left: 120px; top: 190px;
    width: 320px; height: 320px; border-radius: 50%;
    background: radial-gradient(circle, var(--mark-green) 0%, var(--mark-warm) 55%, rgba(255,254,251,0) 72%);
    opacity: 0.8;
  }
  .footer-band {
    position: absolute; left: 0; bottom: 0; width: 560px; height: 150px;
  }
  .tagline {
    font-family: "Lato", sans-serif; font-size: 12px; letter-spacing: 0.6px;
    fill: var(--brand-red); text-transform: uppercase;
  }
</style>
</head>
<body>
<main class="stage">
  <article class="letterhead">
    <header class="brand">
      <span class="brand-dot"></span>
      <span class="brand-name">Corvane<br>Systems</span>
    </header>

    <address class="contact">
      <div class="address">418 Harbor Lane<br>Millbrook, Maryland 21400</div>
      <div class="line">
        <svg viewBox="0 0 10 10"><path d="M2 1 L4 1 L4.6 3 L3.4 3.8 Q4.4 5.8 6.2 6.6 L7 5.4 L9 6 L9 8 Q5 9 2.5 6.5 Q1 4.5 2 1Z" fill="var(--brand-red)"/></svg>
        555-014-2286
      </div>
      <div class="line">
        <svg viewBox="0 0 10 10"><rect x="1" y="3" width="8" height="5" rx="1" fill="var(--brand-red)"/><rect x="3" y="1" width="4" height="2.5" fill="var(--brand-red)"/></svg>
        555-014-2291
      </div>
      <div class="line">
        <svg viewBox="0 0 10 10"><circle cx="5" cy="5" r="4" fill="none" stroke="var(--brand-red)" stroke-width="1.2"/><path d="M1 5 H9 M5 1 Q2.5 5 5 9 Q7.5 5 5 1" fill="none" stroke="var(--brand-red)" stroke-width="0.8"/></svg>
        www.CorvaneSystems.com
      </div>
    </address>

    <div class="watermark" role="img" aria-label="Faint brand emblem of light rays around a recycling symbol and bulb"></div>

    <svg class="footer-band" viewBox="0 0 560 150">
      <path d="M0 30 Q230 140 560 128 L560 150 L0 150 Z" fill="var(--brand-red)"/>
      <path d="M14 16 Q250 118 540 110" fill="none" stroke="var(--brand-blue)" stroke-width="1.5"/>
      <text class="tagline" x="300" y="88" text-anchor="middle">Powering a cleaner tomorrow</text>
    </svg>
  </article>
</main>
</body>
</html>
```